Business Card Design for Fashion Tech Startup

Dear designers, we need a business card for Asia's premier fashion tech startup.!

PebbleHop is discovery e-commerce destination for busy, discerning parents in Asia featuring leading independent designers of baby, kids fashion apparel and sustainable brands from around the world.

PebbleHop is a modern, contemporary fashion tech startup targeting well-educated, well travelled and affluent parents. We're NOT your typical kiddy store!! Our design philosophy & e-commerce site is more like Vask.com, Orimesa.com, Pondwick.com, Farthollow.com.
Updates

Hi, size of the business card should be 84mm X 55mm. Would appreciate some business card layouts in Portrait as added consideration, i fancy the idea of a Portrait business card. What's important is that the business card should pique the receiver's interest to log onto the website to learn more. Many thanks and love forward to the designs!

Target Market(s)

Though modern, classy in look, feel & positioning, PebbleHop does possess a cheeky, fun-loving personality as depicted by its logo and the segment it targets (baby, kids) though the key decision makers i.e primarily mums between 25-40 who are well educated/travelled, local & expatriates, internet/digitally savvy, mid-high income working mums.

Industry/Entity Type

E-Commerce

Requirements
Must have
• Name, designation, email, phone & mobile number.
Company url : www.pebblehop.sg
Slogan : Discovery e-commerce destination for discerning, busy parents
Nice to have
• Call to Action such as a Discount code offering 10% discount
or asking people to "Like" us on our Chatterly page/Chatterly URL

```html
<!DOCTYPE html>
<html lang="en">
<head>
<meta charset="utf-8">
<title>PebbleHop Business Card</title>
<link rel="stylesheet" href="https://fonts.googleapis.com/css2?family=Comic+Neue:wght@400;700&display=swap">
<style>
  :root {
    --coral: #e8675a;
    --navy: #3d5468;
    --cream: #f3efe6;
    --paper: #fbfaf7;
    --stage: #e6e5e2;
    --panel: #ecebea;
    --pattern-a: #f2c7bd;
    --pattern-b: #d9dde2;
  }
  * { box-sizing: border-box; margin: 0; padding: 0; }
  html, body { width: 990px; height: 1200px; overflow: hidden; }
  body {
    background: var(--stage);
    font-family: "Comic Neue", "Comic Sans MS", cursive;
    position: relative;
  }

  /* Card front */
  .card-front {
    position: absolute; left: 135px; top: 40px;
    width: 720px; height: 471px;
    background: var(--cream);
    box-shadow: 0 4px 14px rgba(0,0,0,.18);
    overflow: hidden;
  }
  .card-front .brand {
    position: absolute; left: 60px; top: 42px;
    display: flex; align-items: center; gap: 22px;
  }
  .brand-dot {
    width: 78px; height: 78px; border-radius: 50%;
    border: 9px solid var(--navy);
  }
  .brand-name {
    font-weight: 700; color: var(--coral);
    font-size: 46px; letter-spacing: 1px;
  }
  .contact { position: absolute; left: 60px; top: 170px; color: var(--navy); }
  .contact .person { color: var(--coral); font-weight: 700; font-size: 30px; }
  .contact .role { font-size: 23px; margin-bottom: 10px; }
  .contact ul { list-style: none; font-size: 21px; line-height: 1.3; }
  .contact li { position: relative; padding-left: 22px; }
  .contact li::before {
    content: ""; position: absolute; left: 2px; top: 9px;
    width: 10px; height: 10px; border-radius: 50%; background: var(--coral);
  }
  .contact li.email { color: var(--coral); }
  .like-us {
    position: absolute; left: 60px; bottom: 44px;
    color: var(--coral); font-size: 19px;
  }
  .slogan-band { position: absolute; right: 0; top: 0; width: 150px; height: 471px; }
  .slogan {
    position: absolute; right: 22px; top: 50%;
    transform: translateY(-50%) rotate(90deg);
    transform-origin: center;
    width: 420px; margin-right: -160px;
    text-align: center; color: var(--coral);
    font-weight: 700; font-size: 19px; line-height: 1.25;
  }

  /* Card back */
  .card-back {
    position: absolute; left: 265px; top: 571px;
    width: 460px; height: 301px;
    box-shadow: 0 4px 14px rgba(0,0,0,.18);
    display: flex; overflow: hidden;
  }
  .pattern {
    background: linear-gradient(135deg, var(--pattern-a), var(--pattern-b) 55%, var(--pattern-a));
  }
  .pattern.edge-left { width: 90px; }
  .pattern.middle { width: 250px; position: relative; display: flex; align-items: center; justify-content: center; }
  .pattern.edge-right { width: 30px; }
  .back-dot { width: 150px; height: 150px; border-radius: 50%; border: 14px solid var(--navy); }
  .name-band {
    width: 50px; background: var(--paper);
    border-left: 2px solid #cfd2d6; border-right: 2px solid #cfd2d6;
    display: flex; align-items: center; justify-content: center;
  }
  .name-band span {
    transform: rotate(90deg); white-space: nowrap;
    font-weight: 700; color: var(--coral); font-size: 30px;
  }
  .url-band {
    width: 40px; background: var(--paper);
    display: flex; align-items: center; justify-content: center;
  }
  .url-band span {
    transform: rotate(90deg); white-space: nowrap;
    font-weight: 700; color: var(--navy); font-size: 17px;
  }

  /* Logo sheet */
  .logo-sheet {
    position: absolute; left: 40px; top: 922px;
    width: 910px; height: 238px;
    background: var(--panel);
    display: flex; align-items: center; justify-content: center; gap: 40px;
  }
  .logo-sheet .brand-dot { width: 150px; height: 150px; border-width: 16px; }
  .logo-sheet .brand-name { font-size: 92px; }
</style>
</head>
<body>

<section class="card-front">
  <div class="brand">
    <div class="brand-dot"></div>
    <div class="brand-name">PebbleHop</div>
  </div>
  <div class="contact">
    <p class="person">Name</p>
    <p class="role">designation</p>
    <ul>
      <li class="email">email</li>
      <li>phone &amp; mobile number</li>
      <li>website</li>
    </ul>
  </div>
  <p class="like-us">like us: Chatterly page/Chatterly URL</p>
  <svg class="slogan-band" viewBox="0 0 150 471" aria-hidden="true">
    <path d="M30 0 V190 H18 a32 32 0 0 0 0 64 H30 V471 H150 V0 Z" fill="#ffffff"/>
    <path d="M30 0 V190 H18 a32 32 0 0 0 0 64 H30 V471" fill="none" stroke="#3d5468" stroke-width="8"/>
  </svg>
  <p class="slogan">"Discovery e-commerce destination<br>for discerning, busy parents."</p>
</section>

<section class="card-back">
  <div class="pattern edge-left" role="img" aria-label="Playful pattern of baby clothing and toy silhouettes in coral and navy"></div>
  <div class="name-band"><span>PebbleHop</span></div>
  <div class="pattern middle" role="img" aria-label="Playful pattern of baby clothing and toy silhouettes in coral and navy">
    <div class="back-dot"></div>
  </div>
  <div class="url-band"><span>www.pebblehop.sg</span></div>
  <div class="pattern edge-right" role="img" aria-label="Playful pattern continues to the card edge"></div>
</section>

<section class="logo-sheet">
  <div class="brand-dot"></div>
  <div class="brand-name">PebbleHop</div>
</section>

</body>
</html>
```